Core Values Banner For Hearthwell Partners Inc

We want to take the core values for our small growing chimney service company and post them for our entire team to see on a daily basis. We want to be remind everyone how important this is too us all. IntegrityWe try to be honest and accountable in all aspects of our business, as well as in our personal interactions. We do what we say we will do, when we say we will do it, and how we say we will do it.Kaizen“Change for the best”We strive to constantly grow and improve, both personally and professionally. We own up to our mistakes and strive to resolve and learn from them. We actively seek feedback from our clients and each other. We believe the most innovative ideas come when we intentionally look for them.FamilyWe are a family-owned business, and we consider everyone who works here and every one we serve to be part of the family. Being honest and genuine with each other and our customers is what sets us apart. We put ourselves in our customer’s shoes and make recommendations as if it were our chimney, our home and our family.

Font styles to use
Serif
Sans Serif

Colors
ec1f27

Requirements
Must have
• This banner will be approximately 2.5' in height and 6 to 6.5' in width.
• I would like all 3 core values and there definitions listed on the banner
• check out the feel of our marketing on our website www.hearthwellpartnersvt.example

```html
<!DOCTYPE html>
<html lang="en">
<head>
<meta charset="utf-8">
<title>The Light of Spirit – Hearthwell Partners Inc Core Values</title>
<link rel="stylesheet" href="https://fonts.googleapis.com/css2?family=Roboto:wght@300;700&family=Tinos:wght@400&display=swap">
<style>
  :root {
    --brand-red: #ec1f27;
    --ink: #222222;
    --ink-soft: #333333;
    --paper: #ffffff;
    --frame: #3a3a3a;
    --flame-light: #ffd23f;
    --flame-mid: #f7931e;
    --flame-deep: #e8381e;
  }
  * { box-sizing: border-box; margin: 0; padding: 0; }
  html, body { width: 1200px; height: 401px; overflow: hidden; background: var(--paper); }
  .banner {
    position: relative;
    width: 1200px;
    height: 401px;
    background: var(--paper);
    border: 2px solid var(--frame);
    overflow: hidden;
  }
  .banner-title {
    position: absolute;
    left: 54px;
    top: 50px;
    font-family: "Roboto", Arial, sans-serif;
    font-weight: 700;
    font-size: 60px;
    line-height: 1;
    color: var(--brand-red);
    letter-spacing: -0.5px;
  }
  .banner-subtitle {
    position: absolute;
    left: 54px;
    top: 120px;
    font-family: "Roboto", Arial, sans-serif;
    font-weight: 300;
    font-size: 44px;
    line-height: 1;
    color: var(--ink-soft);
    letter-spacing: -0.5px;
  }
  .value {
    position: absolute;
    top: 222px;
  }
  .value--integrity { left: 54px; width: 250px; }
  .value--change { left: 329px; width: 275px; }
  .value--family { left: 634px; width: 330px; }
  .value-heading {
    font-family: "Tinos", "Times New Roman", serif;
    font-weight: 400;
    font-size: 24px;
    line-height: 26px;
    color: var(--brand-red);
  }
  .value-text {
    font-family: "Tinos", "Times New Roman", serif;
    font-size: 13.4px;
    line-height: 15.6px;
    color: var(--ink);
  }
  .brand-mark {
    position: absolute;
    left: 818px;
    top: 96px;
    width: 160px;
    display: flex;
    flex-direction: column;
    align-items: center;
    gap: 10px;
  }
  .brand-square {
    width: 34px;
    height: 34px;
    background: var(--brand-red);
  }
  .brand-name {
    font-family: "Roboto", Arial, sans-serif;
    font-weight: 700;
    font-size: 19px;
    line-height: 22px;
    text-align: center;
    color: var(--brand-red);
  }
  .torch-art {
    position: absolute;
    left: 1038px;
    top: 10px;
    width: 130px;
    height: 380px;
    border-radius: 60px 60px 20px 20px;
    background: linear-gradient(180deg, var(--flame-deep) 0%, var(--flame-mid) 22%, var(--flame-light) 40%, #f2b233 60%, #e9a23a 80%, #f3c9a8 100%);
  }
</style>
</head>
<body>
  <main class="banner">
    <h1 class="banner-title">The Light of Spirit</h1>
    <p class="banner-subtitle">The Team of Hearthwell Partners</p>

    <section class="value value--integrity">
      <h2 class="value-heading">Integrity</h2>
      <p class="value-text">We try to be honest and accountable in all aspects of our business, as well as in our personal interactions. We do what we say we will do, when we say we will do it, and how we say we will do it.</p>
    </section>

    <section class="value value--change">
      <h2 class="value-heading">Change for the best</h2>
      <p class="value-text">We strive to constantly grow and improve, both personally and professionally. We own up to our mistakes and strive to resolve and learn from them. We actively seek feedback from our clients and each other. We believe the most innovative ideas come when we intentionally look for them.</p>
    </section>

    <section class="value value--family">
      <h2 class="value-heading">Family</h2>
      <p class="value-text">We are a family-owned business, and we consider everyone who works here and every one we serve to be part of the family. Being honest and genuine with each other and our customers is what sets us apart. We put ourselves in our customer’s shoes and make recommendations as if it were our chimney, our home and our family.</p>
    </section>

    <div class="brand-mark">
      <span class="brand-square"></span>
      <span class="brand-name">Hearthwell Partners Inc</span>
    </div>

    <div class="torch-art" role="img" aria-label="Illustration of a raised hand holding a golden torch with a bright flame"></div>
  </main>
</body>
</html>
```